Banner design

Hello.
I require a top header banner for my Interactive and electronic whiteboard / Audio Visual business.
Animated gif.

http://www.qorvantix.com.au

Basically a few photos, my phone number and my new logo (coming soon "Palquestron")
Corporate looking, that immediately captures the customers attention.

Target Market(s)

Adults in Western speaking country (Australia). To young business professionals, teachers, managers etc

Industry/Entity Type

Electronic

```html
<!DOCTYPE html>
<html lang="en">
<head>
<meta charset="utf-8">
<title>Palquestron – eWhiteboards + Audio Visual</title>
<link rel="stylesheet" href="https://fonts.googleapis.com/css2?family=Cabin:wght@400;600&display=swap">
<style>
  :root {
    --bg: #000000;
    --panel: #ffffff;
    --brand-grey: #5f5f5f;
    --tagline-grey: #858585;
    --text-grey: #555555;
    --photo-light: #eef0f2;
    --photo-mid: #b9bec5;
    --photo-dark: #7d848c;
  }
  * { margin: 0; padding: 0; box-sizing: border-box; }
  html, body {
    width: 1200px;
    height: 900px;
    overflow: hidden;
    background: var(--bg);
  }
  .banner {
    position: relative;
    width: 1200px;
    height: 900px;
    background: var(--bg);
    font-family: "Cabin", sans-serif;
  }
  .brand {
    position: absolute;
    top: 76px;
    left: 0;
    width: 1200px;
    text-align: center;
  }
  .brand-name {
    display: inline-block;
    font-size: 92px;
    font-weight: 600;
    letter-spacing: 17px;
    margin-right: -17px;
    line-height: 1;
    color: var(--brand-grey);
    text-transform: uppercase;
  }
  .brand-tagline {
    margin-top: 8px;
    font-size: 38px;
    font-weight: 400;
    letter-spacing: 3px;
    color: var(--tagline-grey);
  }
  .panel {
    position: absolute;
    left: 120px;
    width: 960px;
    height: 143px;
    background: var(--panel);
    overflow: hidden;
  }
  .panel-learning { top: 269px; }
  .panel-meetings { top: 473px; }
  .panel-contact  { top: 677px; }
  .panel-photo {
    position: absolute;
    top: 0;
    height: 100%;
    width: 410px;
  }
  .panel-learning .panel-photo {
    left: 0;
    background: linear-gradient(90deg, var(--photo-dark) 0%, var(--photo-mid) 45%, var(--photo-light) 80%, var(--panel) 100%);
  }
  .panel-meetings .panel-photo {
    right: 0;
    width: 408px;
    background: linear-gradient(90deg, var(--panel) 0%, var(--photo-light) 25%, var(--photo-mid) 70%, var(--photo-dark) 100%);
  }
  .panel-label {
    position: absolute;
    top: 50%;
    transform: translateY(-50%);
    font-size: 41px;
    font-weight: 400;
    letter-spacing: 1.5px;
    color: var(--text-grey);
    white-space: nowrap;
  }
  .panel-learning .panel-label { left: 430px; }
  .panel-meetings .panel-label { left: 100px; }
  .contact-lines {
    position: absolute;
    inset: 0;
    display: flex;
    flex-direction: column;
    justify-content: center;
    align-items: center;
    font-size: 38px;
    font-style: normal;
    line-height: 1.15;
    letter-spacing: 2px;
    color: var(--text-grey);
  }
</style>
</head>
<body>
  <main class="banner">
    <header class="brand">
      <div class="brand-name">Palquestron</div>
      <p class="brand-tagline">eWhiteboards + Audio Visual</p>
    </header>

    <section class="panel panel-learning">
      <div class="panel-photo" role="img" aria-label="Photo of a teacher and students in a classroom with an interactive whiteboard"></div>
      <h2 class="panel-label">Learning + Education</h2>
    </section>

    <section class="panel panel-meetings">
      <h2 class="panel-label">Meetings + Proposals</h2>
      <div class="panel-photo" role="img" aria-label="Photo of a businesswoman presenting a chart on an electronic whiteboard"></div>
    </section>

    <section class="panel panel-contact">
      <address class="contact-lines">
        <span class="contact-email">e: mail@qorvantix.com.au</span>
        <span class="contact-phones">m: 0491 570 318 p: (02) 5550 7294</span>
      </address>
    </section>
  </main>
</body>
</html>
```